Buch-/eBook-Cover für Esoterikbuch
Alle meine Änderungswünsche wurden zeitnah umgesetzt. Als es nach der Dateiübergabe technische Probleme gab, weil ich den Buchinhalt falsch formatiert hatte, hat die Designerin viel Geduld bewiesen und das Cover dann klaglos an die neuen Formate angepasst. Ich werde jederzeit gerne wieder mit ihr zusammenarbeiten.
Zielgruppe
Ebook- und Taschenbuchcover für ein Esoterikbuch über Quantenheilung auf Lesora. Details befinden sich im Anhang.
Aufgabenstellung
Keine besonderen Vorgaben.

```html
<!DOCTYPE html>
<html lang="de">
<head>
<meta charset="utf-8">
<title>Quantenheilung und Bewusstsein – Buchumschlag</title>
<link rel="stylesheet" href="https://fonts.googleapis.com/css2?family=Saira+Semi+Condensed:wght@400;600;700&family=Sarabun:wght@300;400&display=swap">
<style>
  :root {
    --page: #ffffff;
    --navy: #161d38;
    --ink-light: #ffffff;
    --ink-soft: #e8ecf6;
    --spine-line: #4a5a86;
  }
  * { box-sizing: border-box; margin: 0; padding: 0; }
  html, body { width: 1200px; height: 810px; overflow: hidden; background: var(--page); }
  .canvas { position: relative; width: 1200px; height: 810px; }

  .wraparound {
    position: absolute; left: 169px; top: 70px; width: 862px; height: 671px;
    background: var(--navy);
    box-shadow: 0 6px 28px rgba(0,0,0,0.18);
    overflow: hidden;
  }

  .back-visual {
    position: absolute; left: 53px; top: 420px; width: 302px; height: 160px;
    background:
      radial-gradient(ellipse 28% 30% at 48% 38%, rgba(190,220,255,0.85), rgba(90,150,240,0.4) 55%, transparent 75%),
      radial-gradient(ellipse 55% 35% at 50% 62%, rgba(60,130,230,0.55), transparent 75%),
      radial-gradient(ellipse 60% 50% at 50% 55%, rgba(40,70,160,0.45), transparent 80%);
  }
  .barcode-field { position: absolute; left: 60px; top: 562px; width: 111px; height: 67px; background: #ffffff; }

  .spine { position: absolute; left: 420px; top: 0; width: 22px; height: 100%; border-left: 1px solid var(--spine-line); border-right: 1px solid var(--spine-line); }

  .front-artwork {
    position: absolute; left: 442px; top: 0; width: 420px; height: 100%;
    background:
      radial-gradient(ellipse 45% 22% at 55% 22%, rgba(229,154,60,0.55), transparent 75%),
      radial-gradient(ellipse 55% 30% at 75% 55%, rgba(111,224,240,0.45), transparent 75%),
      radial-gradient(ellipse 60% 35% at 80% 75%, rgba(63,166,224,0.45), transparent 75%),
      radial-gradient(ellipse 30% 45% at 15% 55%, rgba(200,140,100,0.55), transparent 80%),
      linear-gradient(180deg, #141c3c 0%, #1f3a6a 40%, #24507e 65%, #141c3c 100%);
  }

  .cover-type { position: absolute; left: 0; top: 0; width: 862px; height: 671px; }
  .cover-type text { fill: var(--ink-light); }
  .display { font-family: "Saira Semi Condensed", "Arial Narrow", sans-serif; }
  .display-bold { font-weight: 700; }
  .display-semi { font-weight: 600; }
  .display-regular { font-weight: 400; }
  .blurb-line { font-family: "Sarabun", sans-serif; font-weight: 300; font-size: 13.5px; fill: var(--ink-soft); }
  .spine-line-text { font-family: "Sarabun", sans-serif; font-weight: 400; font-size: 13px; }
</style>
</head>
<body>
<div class="canvas">
  <div class="wraparound">
    <div class="back-visual" role="img" aria-label="Leuchtendes Gehirn über einem blauen Netzwerk aus Punkten und Linien"></div>
    <div class="barcode-field"></div>
    <div class="spine"></div>
    <div class="front-artwork" role="img" aria-label="Profil einer Person mit geschlossenen Augen, umgeben von fließenden blauen und goldenen Lichtwellen"></div>

    <svg class="cover-type" viewBox="0 0 862 671" xmlns="http://www.w3.org/2000/svg">
      <!-- Back cover title -->
      <g class="back-title">
        <text class="display display-bold" x="62" y="73.5" font-size="33" textLength="192" lengthAdjust="spacingAndGlyphs">Quantenheilung</text>
        <text class="display display-regular" x="62" y="101.5" font-size="26" textLength="192" lengthAdjust="spacingAndGlyphs">und Bewusstsein</text>
      </g>

      <!-- Back cover blurb -->
      <g class="blurb">
        <text class="blurb-line" x="62" y="141.7" textLength="315" lengthAdjust="spacingAndGlyphs">Willkommen in der subatomaren Welt aus Quarks und</text>
        <text class="blurb-line" x="62" y="162.7" textLength="298" lengthAdjust="spacingAndGlyphs">Strings, wo reines Bewusstsein und reine Informa-</text>
        <text class="blurb-line" x="62" y="183.7" textLength="293" lengthAdjust="spacingAndGlyphs">tionen unabhängig von Zeit und Raum das Dasein</text>
        <text class="blurb-line" x="62" y="204.7" textLength="69" lengthAdjust="spacingAndGlyphs">bestimmen.</text>

        <text class="blurb-line" x="62" y="232.6" textLength="305" lengthAdjust="spacingAndGlyphs">Seit Jahrhunderten wird die Quantenheilung erfolg-</text>
        <text class="blurb-line" x="62" y="253.6" textLength="304" lengthAdjust="spacingAndGlyphs">reich praktiziert, wenn auch unter anderem Namen.</text>
        <text class="blurb-line" x="62" y="274.6" textLength="295" lengthAdjust="spacingAndGlyphs">Erst in den letzten Jahren ist es der Wissenschaft</text>
        <text class="blurb-line" x="62" y="295.6" textLength="285" lengthAdjust="spacingAndGlyphs">gelungen, die Wirkungsweise dieser uralten Hei-</text>
        <text class="blurb-line" x="62" y="316.6" textLength="307" lengthAdjust="spacingAndGlyphs">lungsmethode mit modernen Erkenntnissen aus der</text>
        <text class="blurb-line" x="62" y="337.6" textLength="309" lengthAdjust="spacingAndGlyphs">Quantenphysik in Verbindung zu bringen. Die daraus</text>
        <text class="blurb-line" x="62" y="358.6" textLength="305" lengthAdjust="spacingAndGlyphs">resultierenden Schlussfolgerungen und erweiterten</text>
        <text class="blurb-line" x="62" y="379.6" textLength="309" lengthAdjust="spacingAndGlyphs">Heilungstechniken wird dieses Buch Ihnen unter Be-</text>
        <text class="blurb-line" x="62" y="400.6" textLength="314" lengthAdjust="spacingAndGlyphs">zug auf wissenschaftliche Methodik und Verfahrens-</text>
        <text class="blurb-line" x="62" y="421.6" textLength="171" lengthAdjust="spacingAndGlyphs">weisen ausführlich darlegen.</text>
      </g>

      <!-- Spine -->
      <g class="spine-type">
        <text class="spine-line-text" transform="translate(434 173) rotate(-90)" x="0" y="0" textLength="127" lengthAdjust="spacingAndGlyphs">Konrad Sternfeld</text>
        <text class="spine-line-text" transform="translate(434 492) rotate(-90)" x="0" y="0" textLength="204" lengthAdjust="spacingAndGlyphs">Quantenheilung  und  Bewusstsein</text>
      </g>

      <!-- Front cover -->
      <g class="front-title">
        <text class="display display-bold" x="484" y="87.5" font-size="62" textLength="335" lengthAdjust="spacingAndGlyphs">Quantenheilung</text>
        <text class="display display-regular" x="484" y="135.5" font-size="48" textLength="335" lengthAdjust="spacingAndGlyphs">und Bewusstsein</text>
      </g>
      <g class="front-subtitle">
        <text class="display display-semi" x="615" y="198.3" font-size="22" textLength="166" lengthAdjust="spacingAndGlyphs">Wie Sie Zugriff auf</text>
        <text class="display display-semi" x="615" y="225.2" font-size="22" textLength="204" lengthAdjust="spacingAndGlyphs">die Informationsebene</text>
        <text class="display display-semi" x="615" y="252" font-size="22" textLength="183" lengthAdjust="spacingAndGlyphs">der Realität nehmen</text>
      </g>
      <text class="display display-semi front-author" x="561" y="626.6" font-size="23" textLength="181" lengthAdjust="spacingAndGlyphs">Konrad Sternfeld</text>
    </svg>
  </div>
</div>
</body>
</html>
```